4R Capital business cards for a tech VC

We're starting a new Venture Capital that is focusing on bringing the best start ups from Israel to NYC
We need a business cards template for this that gives the sense of an entrepreneurial look
I don't want any religious signs on this even thought it's Israel
I'm looking for a techi feeling but not too crazy
The card should probably be in the same light blue as the logo and the logo in white

Target Market(s)

Investors

Industry/Entity Type

Tech

Contact Information for Business Card

The card needs to look slick and entrepreneurship like
The VC is focused on NYC and Tel Aviv so could be great to show something on the back side that is like NYC skyline or something like that
You can see the logo attached

Colors
0455a3
3276b5
85acd3
cedeed
eaf1f7

Requirements
Must have
• A very cool looking business card that shows we're a cutting edge tech VC with a focus on bringing start ups from Tel Aviv and leveraging the NYC ecosystem
Nice to have
• NYC skyline can be cool , maybe something that is connected to Tel Aviv

```html
<!DOCTYPE html>
<html lang="en">
<head>
<meta charset="utf-8">
<title>4R Capital Business Cards</title>
<link rel="stylesheet" href="https://fonts.googleapis.com/css2?family=Lato:wght@400;700;900&display=swap">
<style>
  :root {
    --brand-blue: #3276b5;
    --brand-deep: #0455a3;
    --brand-bright: #1a8fd0;
    --brand-soft: #85acd3;
    --ink: #1d1d1f;
    --paper: #ffffff;
    --backdrop: #e9edf1;
  }
  * { margin: 0; padding: 0; box-sizing: border-box; }
  html, body {
    width: 1200px; height: 900px; overflow: hidden;
    background: var(--backdrop);
    font-family: "Lato", sans-serif;
  }
  .canvas { position: relative; width: 1200px; height: 900px; }

  .card {
    position: absolute;
    width: 620px; height: 354px;
    overflow: hidden;
    box-shadow: 0 10px 30px rgba(0,0,0,0.18);
  }

  /* Back side */
  .card-back { left: 520px; top: 60px; background: var(--brand-blue); }
  .skyline-area {
    position: absolute; left: 0; right: 0; bottom: 0; height: 170px;
    background: linear-gradient(180deg, rgba(26,143,208,0) 0%, var(--brand-bright) 45%, var(--brand-bright) 100%);
  }
  .back-brand {
    position: absolute; left: 0; right: 0; top: 118px;
    text-align: center;
    color: var(--paper);
    font-weight: 900; font-size: 58px; letter-spacing: 2px;
    text-transform: uppercase;
  }
  .back-web {
    position: absolute; left: 0; right: 0; top: 212px;
    text-align: center; color: var(--paper);
    font-size: 17px; letter-spacing: 1.5px;
  }

  /* Front side */
  .card-front { left: 70px; top: 470px; background: var(--paper); }
  .front-wave { position: absolute; left: 0; top: 0; width: 620px; height: 354px; }
  .front-brand {
    position: absolute; left: 36px; top: 78px; width: 300px;
    color: var(--brand-blue);
    font-weight: 900; font-size: 44px; letter-spacing: 1.5px;
    text-transform: uppercase; line-height: 1;
  }
  .front-brand .mark {
    display: inline-block; width: 22px; height: 22px;
    background: var(--brand-blue); margin-right: 12px; vertical-align: 4px;
  }
  .divider {
    position: absolute; left: 342px; top: 44px;
    width: 2px; height: 170px; background: var(--brand-blue);
  }
  .contact { position: absolute; left: 372px; top: 50px; color: var(--ink); }
  .contact-name { color: var(--brand-blue); font-weight: 700; font-size: 24px; line-height: 1.1; }
  .contact-role { font-size: 15px; margin-bottom: 10px; }
  .contact-address { font-size: 16px; line-height: 1.3; margin-bottom: 6px; }
  .contact-line { display: flex; align-items: center; font-size: 16px; line-height: 1.45; }
  .contact-line svg { width: 16px; height: 16px; margin-right: 10px; fill: var(--brand-blue); flex: none; }
  .front-web {
    position: absolute; left: 150px; top: 300px;
    color: var(--paper); font-size: 17px; letter-spacing: 1.2px;
  }
</style>
</head>
<body>
<main class="canvas">

  <section class="card card-back">
    <div class="skyline-area" role="img" aria-label="New York City skyline silhouette with the Statue of Liberty in lighter blue"></div>
    <div class="back-brand">4R Capital</div>
    <div class="back-web">www.4rcapital.com</div>
  </section>

  <section class="card card-front">
    <svg class="front-wave" viewBox="0 0 620 354" preserveAspectRatio="none" aria-hidden="true">
      <path d="M0 236 C 220 250, 420 300, 620 354 L0 354 Z" fill="var(--brand-blue)"/>
      <path d="M0 228 C 230 240, 430 290, 620 340 L620 348 C 430 298, 230 250, 0 240 Z" fill="var(--brand-bright)"/>
      <path d="M0 240 C 230 250, 430 298, 620 348 L620 354 C 430 304, 230 256, 0 246 Z" fill="var(--paper)"/>
    </svg>

    <div class="front-brand"><span class="mark"></span>4R Capital</div>
    <div class="divider"></div>

    <div class="contact">
      <div class="contact-name">Daniel Morrow</div>
      <div class="contact-role">Manager</div>
      <div class="contact-address">1450 Harbor Lane<br>Austin TX 78010</div>
      <div class="contact-line">
        <svg viewBox="0 0 24 24"><path d="M6.6 10.8a15.1 15.1 0 0 0 6.6 6.6l2.2-2.2a1 1 0 0 1 1-.25 11.4 11.4 0 0 0 3.6.57 1 1 0 0 1 1 1V20a1 1 0 0 1-1 1A17 17 0 0 1 3 4a1 1 0 0 1 1-1h3.5a1 1 0 0 1 1 1c0 1.25.2 2.45.57 3.57a1 1 0 0 1-.25 1z"/></svg>
        512 000 4410
      </div>
      <div class="contact-line">
        <svg viewBox="0 0 24 24"><path d="M7 3h10v4H7zM4 8h16a2 2 0 0 1 2 2v6h-4v5H6v-5H2v-6a2 2 0 0 1 2-2zm4 8v3h8v-3z"/></svg>
        512 000 4411
      </div>
      <div class="contact-line">
        <svg viewBox="0 0 24 24"><path d="M2 5h20v14H2zm2 2v.5l8 5 8-5V7zm0 2.8V17h16V9.8l-8 5z"/></svg>
        hello@4rcapital.com
      </div>
    </div>

    <div class="front-web">www.4rcapital.com</div>
  </section>

</main>
</body>
</html>
```